Luma Harbor Vow Studio, Inc.

Luma Harbor Vow Studio Business Card design for Cardlyne. Clean, contemporary, creative, colorful (using colors provided). ONE SIDE SHOULD INCLUDE logo, www.lumaharborvowstudio.com, @sayidoatluma. OTHER SIDE SHOULD INCLUDE Delia Brennan. Owner & Officiant. Marisol Cove, Costa Luma. 555.014.2871. delia@lumaharborvowstudio.com. Colors are blue #58AA9E
and golden #e2bf80)

Target Market(s)

Destination Wedding Clients in the United States

Contact Information for Business Card

Delia Brennan
Owner & Officiant
Marisol Cove, Costa Luma
555.014.2871
delia@lumaharborvowstudio.com

Font styles to use
Sans Serif

Requirements
Must have
• Colorful (colors are blue #58AA9E
• and golden #e2bf80), clean, contemporary. ONE SIDE SHOULD INCLUDE logo, www.lumaharborvowstudio.com, @sayidoatluma. Other side should include Delia Brennan. Owner & Officiant. Marisol Cove, Costa Luma. 555.014.2871. delia@lumaharborvowstudio.com
Nice to have
• I would like to see a version that includes my bio photo, and one that doesn't include the bio photo

```html
<!DOCTYPE html>
<html lang="en">
<head>
<meta charset="utf-8">
<title>Luma Harbor Vow Studio – Business Card</title>
<link href="https://fonts.googleapis.com/css2?family=Lato:wght@300;400;700;900&family=Quicksand:wght@400;500&display=swap" rel="stylesheet">
<style>
  :root {
    --teal: #58aa9e;
    --gold: #e2bf80;
    --white: #ffffff;
    --stage: #2b2d2f;
    --photo-warm: #d9a66f;
    --photo-cool: #9a9c9e;
  }
  * { margin: 0; padding: 0; box-sizing: border-box; }
  html, body { width: 1200px; height: 900px; overflow: hidden; }
  body {
    background: var(--stage);
    font-family: "Lato", sans-serif;
    position: relative;
  }
  .card {
    position: absolute;
    left: 320px;
    width: 560px;
    height: 320px;
    border-radius: 28px;
    overflow: hidden;
    background: var(--teal);
    color: var(--white);
  }
  .card--brand { top: 100px; }
  .card--person { top: 480px; }

  /* Brand side */
  .brand-panel {
    position: absolute; inset: 0;
    background: var(--white);
    clip-path: polygon(0 0, 42% 0, 54% 100%, 0 100%);
  }
  .brand-name {
    position: absolute;
    left: 38px; top: 118px;
    width: 190px;
    font-weight: 400;
    font-size: 26px;
    line-height: 1.15;
    letter-spacing: 1px;
    color: var(--gold);
    text-align: center;
  }
  .social-handle {
    position: absolute;
    left: 290px; top: 112px;
    font-family: "Quicksand", sans-serif;
    font-size: 17px;
    letter-spacing: 0.5px;
  }
  .web-band {
    position: absolute;
    left: 262px; right: 0; top: 140px;
    height: 30px;
    background: var(--white);
    clip-path: polygon(8px 0, 100% 0, 100% 100%, 0 100%);
    color: var(--teal);
    font-weight: 700;
    font-size: 16px;
    letter-spacing: 0.3px;
    line-height: 30px;
    padding-left: 28px;
  }
  .web-rule {
    position: absolute;
    left: 268px; right: 0; top: 178px;
    height: 3px;
    background: var(--white);
    opacity: 0.85;
  }

  /* Person side */
  .photo-frame {
    position: absolute; inset: 0;
    background: var(--white);
    clip-path: polygon(56% 0, 100% 0, 100% 100%, 68% 100%);
  }
  .photo {
    position: absolute; inset: 0;
    background: radial-gradient(ellipse at 62% 70%, var(--photo-cool) 0 30%, transparent 31%),
                linear-gradient(135deg, #e8b67c, var(--photo-warm));
    clip-path: polygon(57.5% 0, 100% 0, 100% 100%, 69.5% 100%);
  }
  .person-name {
    position: absolute;
    left: 0; width: 312px; top: 72px;
    text-align: right;
    font-size: 31px;
    letter-spacing: 0.5px;
    line-height: 1;
    white-space: nowrap;
  }
  .person-name__first { font-weight: 300; }
  .person-name__last { font-weight: 900; }
  .person-role {
    position: absolute;
    left: 118px; top: 112px;
    width: 200px; height: 32px;
    background: var(--white);
    color: var(--teal);
    font-family: "Quicksand", sans-serif;
    font-size: 18px;
    line-height: 32px;
    text-align: right;
    padding-right: 12px;
    white-space: nowrap;
  }
  .contact-list {
    position: absolute;
    right: 218px; bottom: 36px;
    list-style: none;
    text-align: right;
    font-size: 15px;
    line-height: 1.55;
    font-weight: 400;
  }
  .contact-list li { display: flex; justify-content: flex-end; align-items: center; gap: 8px; white-space: nowrap; }
  .contact-list svg { width: 13px; height: 13px; fill: var(--white); }
  .contact-list .no-icon { padding-right: 21px; }
</style>
</head>
<body>

  <section class="card card--brand" aria-label="Business card, brand side">
    <div class="brand-panel"></div>
    <p class="brand-name">Luma Harbor Vow Studio</p>
    <p class="social-handle">@sayidoatluma</p>
    <p class="web-band">www.lumaharborvowstudio.com</p>
    <div class="web-rule"></div>
  </section>

  <section class="card card--person" aria-label="Business card, contact side">
    <div class="photo-frame"></div>
    <div class="photo" role="img" aria-label="Portrait photo of Delia Brennan"></div>
    <h1 class="person-name"><span class="person-name__first">DELIA </span><span class="person-name__last">BRENNAN</span></h1>
    <p class="person-role">Owner &amp; Officiant</p>
    <ul class="contact-list">
      <li>555.014.2871
        <svg viewBox="0 0 16 16" aria-hidden="true"><path d="M3.5 1l3 3-1.8 1.8c.8 1.9 2.6 3.7 4.5 4.5L11 8.5l3 3-2 2.5C6.5 13.5 2.5 9.5 1 3.5z"/></svg>
      </li>
      <li>delia@lumaharborvowstudio.com
        <svg viewBox="0 0 16 16" aria-hidden="true"><path d="M1 3h14v10H1z M2 4.2v.4l6 4.2 6-4.2v-.4z" fill-rule="evenodd"/></svg>
      </li>
      <li class="no-icon">Marisol Cove, Costa Luma</li>
    </ul>
  </section>

</body>
</html>
```